UsPoint Building Bonds across a proven circle

I am looking for a sleek, clean and simple app design. I need also a payment page and offering different packages and payment types.

I would like the color scheme to be black or white very futuristic like the movie z-droner.

The profile page displaying the picture, as clean and future like as possible.

Share profile options, manage subscription, update profile, help ect….

On the verified page last one, the social media logos are interactive so the user can share their info through the connected social media account.

Target Market(s)

Professionals and individuals.

Industry/Entity Type

Due diligence & background checks verification

Font styles to use
Sans Serif

Colors
0054AA
0677BA
7BADD7
CADEEF
E8F1F8
0094D4
00A9DD
6FCCEA
C7EBF8
E9F6FB
59FF00
82FF00
B8FF75
E3FFCB
F4FFEA

Requirements
Must have
• The ability to add my social media links or log in through the app directly for direct confirmation. After email entered on account sign up they get either a confirmation email or a text through telephone number verification.
Nice to have
• Account creation to add profile picture must take a selfie.

```html
<!DOCTYPE html>
<html lang="en">
<head>
<meta charset="utf-8">
<title>UsPoint – Create Username</title>
<link rel="stylesheet" href="https://fonts.googleapis.com/css2?family=Montserrat:wght@400;500;700&display=swap">
<style>
  :root {
    --canvas-bg: #edf3fb;
    --screen-bg: #e1eaf7;
    --surface: #eaf1fb;
    --shadow-dark: rgba(150, 170, 200, 0.45);
    --shadow-light: rgba(255, 255, 255, 0.95);
    --text-muted: #a3afc1;
    --text-soft: #b3bdcc;
    --brand-deep: #2b4e8e;
    --brand-accent: #6fccea;
    --icon: #8ea0bb;
  }
  * { box-sizing: border-box; margin: 0; padding: 0; }
  html, body {
    width: 1200px; height: 1168px; overflow: hidden;
    background: var(--canvas-bg);
    font-family: "Montserrat", sans-serif;
  }
  .app-screen {
    position: absolute; left: 390px; top: 114px;
    width: 420px; height: 940px;
    background: var(--screen-bg);
    border-radius: 56px;
    box-shadow: 14px 18px 40px var(--shadow-dark), -10px -10px 30px var(--shadow-light);
    overflow: hidden;
  }
  .brand-pill {
    position: absolute; right: 22px; top: 60px;
    width: 230px; height: 92px; border-radius: 46px;
    background: #f3f7fd;
    box-shadow: 6px 8px 18px var(--shadow-dark), -6px -6px 14px var(--shadow-light);
    display: flex; align-items: center; justify-content: center; gap: 12px;
  }
  .brand-dot { width: 22px; height: 22px; border-radius: 50%; background: var(--brand-accent); }
  .brand-name { font-weight: 700; font-size: 32px; color: var(--brand-deep); letter-spacing: 1px; }

  .stepper { position: absolute; left: 0; top: 190px; width: 100%; height: 150px; }
  .step {
    position: absolute; width: 52px; height: 52px; border-radius: 50%;
    background: var(--surface);
    box-shadow: 5px 6px 12px var(--shadow-dark), -5px -5px 10px var(--shadow-light);
    display: flex; align-items: center; justify-content: center;
    color: var(--icon); font-weight: 500; font-size: 18px;
  }
  .step-one { left: 60px; top: 20px; }
  .step-two { left: 184px; top: 78px; }
  .step-three { left: 308px; top: 20px; }
  .step-connector { position: absolute; left: 0; top: 0; }
  .step-label {
    position: absolute; left: 174px; top: 44px;
    font-size: 11px; letter-spacing: 0.5px; color: var(--text-muted);
  }

  .title {
    position: absolute; top: 380px; width: 100%; text-align: center;
    font-size: 13px; font-weight: 500; letter-spacing: 0.6px; color: var(--text-muted);
  }
  .username-field {
    position: absolute; left: 50px; top: 420px; width: 320px; height: 80px;
    border-radius: 40px; background: var(--screen-bg);
    box-shadow: inset 6px 6px 12px var(--shadow-dark), inset -6px -6px 12px var(--shadow-light);
    display: flex; align-items: center; padding-left: 34px;
    font-size: 12px; letter-spacing: 0.5px; color: var(--text-muted);
  }
  .rules { position: absolute; left: 58px; top: 528px; list-style: none; }
  .rules li { font-size: 11px; color: var(--text-soft); line-height: 22px; }
  .rules li::before { content: "• "; }

  .next-row {
    position: absolute; bottom: 60px; left: 0; width: 100%;
    display: flex; align-items: center; justify-content: center; gap: 18px;
  }
  .next-label { font-size: 11px; letter-spacing: 0.5px; color: var(--text-muted); }
  .next-button {
    width: 56px; height: 56px; border-radius: 50%; background: var(--surface);
    box-shadow: 6px 7px 14px var(--shadow-dark), -5px -5px 12px var(--shadow-light);
    display: flex; align-items: center; justify-content: center;
  }
</style>
</head>
<body>
  <main class="app-screen">
    <div class="brand-pill">
      <span class="brand-dot"></span>
      <span class="brand-name">UsPoint</span>
    </div>

    <div class="stepper">
      <svg class="step-connector" width="420" height="150" viewBox="0 0 420 150">
        <path d="M108 50 L188 100 M260 100 L314 50" stroke="#aab7ca" stroke-width="1.2" stroke-dasharray="4 4" fill="none"/>
      </svg>
      <div class="step step-one">
        <svg width="20" height="20" viewBox="0 0 20 20" fill="none" stroke="var(--icon)" stroke-width="1.6" stroke-linecap="round">
          <path d="M16 10a6 6 0 1 1-2-4.5"/><path d="M7 10l2.5 2.5L16 6"/>
        </svg>
      </div>
      <span class="step-label">USERNAME</span>
      <div class="step step-two">2</div>
      <div class="step step-three">
        <svg width="18" height="18" viewBox="0 0 18 18" fill="none" stroke="var(--icon)" stroke-width="1.6" stroke-linecap="round" stroke-linejoin="round">
          <path d="M4 9h10M10 5l4 4-4 4"/>
        </svg>
      </div>
    </div>

    <h1 class="title">CREATE A UNIQUE USPOINT USERNAME</h1>
    <div class="username-field">USERNAME</div>
    <ul class="rules">
      <li>Must be 3 to 20 characters long.</li>
      <li>Letter and numbers only.</li>
      <li>Spcial characters and spaces are not valid.</li>
    </ul>

    <div class="next-row">
      <span class="next-label">NEXT</span>
      <div class="next-button">
        <svg width="18" height="18" viewBox="0 0 18 18" fill="none" stroke="var(--icon)" stroke-width="1.6" stroke-linecap="round" stroke-linejoin="round">
          <path d="M4 9h10M10 5l4 4-4 4"/>
        </svg>
      </div>
    </div>
  </main>
</body>
</html>
```